Email Signiture and letterhead design

we are looking for a modern business design to incorporate our logo and qel certification plus social icons for Vorlant, Pelmora, and zandoro
they must include our UK vat and also company registration as text but I can fill these out. Email signature to have a link/icon to our webshop www.trexolan.co.uk

Target Market(s)

All

Font styles to use
Serif
Sans Serif

Requirements
Must have
• Address, tel, email , web details incorperated
Nice to have
• a professional looking letter head and email signiture, Email signature to have a link/icon to our webshop www.trexolan.co.uk

```html
<!DOCTYPE html>
<html lang="en">
<head>
<meta charset="utf-8">
<title>Trexolan Bearings Ltd – Letterhead and Email Signature</title>
<link href="https://fonts.googleapis.com/css2?family=Montserrat:wght@400;500;600&family=Roboto+Condensed:wght@400;700&display=swap" rel="stylesheet">
<style>
  :root {
    --red: #e8202a;
    --dark: #3a3a3a;
    --ink: #2b2b2b;
    --page: #ffffff;
    --backdrop: #c6c6c6;
    --badge-pink: #e0137f;
  }
  * { margin: 0; padding: 0; box-sizing: border-box; }
  html, body { width: 1200px; height: 1200px; overflow: hidden; }
  body { background: var(--backdrop); position: relative; font-family: "Montserrat", sans-serif; color: var(--ink); }

  .brand { display: flex; align-items: center; gap: 6px; color: var(--dark); font-weight: 500; white-space: nowrap; }
  .brand-dot { border-radius: 50%; background: var(--red); flex: none; }
  .contact-line { display: flex; align-items: center; gap: 3px; white-space: nowrap; }
  .contact-line svg { flex: none; }
  .web-accent { color: var(--red); }

  /* Letterhead */
  .letterhead {
    position: absolute; left: 78px; top: 60px; width: 485px; height: 732px;
    background: var(--page); overflow: hidden;
    box-shadow: 0 2px 8px rgba(0,0,0,.18);
  }
  .letterhead .brand { position: absolute; left: 27px; top: 60px; font-size: 14.5px; }
  .letterhead .brand-dot { width: 16px; height: 16px; }

  .lh-contact {
    position: absolute; left: 347px; top: 18px; height: 66px;
    border-left: 1.5px solid var(--red); padding-left: 10px;
    font-size: 8.6px; line-height: 13.2px; color: var(--ink);
  }
  .lh-rule { position: absolute; left: 24px; top: 92px; width: 443px; height: 1.5px; background: var(--red); }

  .letter { position: absolute; left: 24px; top: 156px; width: 445px; font-family: "Roboto Condensed", sans-serif; color: var(--ink); }
  .letter-date { font-family: "Montserrat", sans-serif; font-weight: 600; font-size: 9.5px; }
  .letter-to { margin-top: 22px; font-size: 9px; }
  .recipient-name { margin-top: 14px; font-weight: 700; font-size: 11px; }
  .recipient-detail { font-size: 8px; line-height: 15px; margin-top: 3px; }
  .letter-body { margin-top: 27px; font-size: 7.4px; line-height: 14.9px; color: #333; }
  .letter-body p + p { margin-top: 14.9px; }
  .sign-off { margin-top: 26px; font-size: 9px; }
  .signature-area { width: 110px; height: 72px; margin-top: 14px; background: #f1f1f1; }

  .lh-social { position: absolute; left: 362px; top: 606px; display: flex; gap: 4px; }
  .lh-social-item { display: flex; align-items: center; gap: 2px; font-size: 4.6px; color: var(--red); font-weight: 600; }
  .lh-social-item i { width: 12px; height: 12px; border-radius: 50%; background: var(--red); display: block; }
  .cert-badge { position: absolute; left: 387px; top: 628px; width: 72px; height: 27px; border: 1px solid #bbb; border-radius: 4px; background: #fff; overflow: hidden; }
  .cert-badge::after { content: ""; position: absolute; right: 0; top: 0; width: 8px; height: 100%; background: var(--badge-pink); }
  .cert-number { position: absolute; left: 385px; top: 659px; font-size: 5.8px; color: #444; white-space: nowrap; }
  .lh-wave { position: absolute; left: 0; bottom: 0; }

  /* Email signature */
  .signature-card {
    position: absolute; width: 1088px; height: 331px; background: var(--page); overflow: hidden;
    box-shadow: 0 3px 10px rgba(0,0,0,.2);
  }
  .signature-card.large { left: 50px; top: 823px; }
  .signature-card.small { left: 494px; top: 301px; transform: scale(0.5836); transform-origin: top left; }
  .signature-card .brand { position: absolute; left: 118px; top: 170px; font-size: 33px; }
  .signature-card .brand-dot { width: 34px; height: 34px; }
  .sig-divider { position: absolute; left: 547px; top: 32px; width: 2.5px; height: 233px; background: var(--red); }
  .sig-details { position: absolute; left: 571px; top: 28px; color: var(--ink); }
  .sig-name { font-size: 27px; font-weight: 600; color: var(--red); line-height: 32px; letter-spacing: .3px; }
  .sig-role { font-size: 19px; line-height: 26px; margin-top: 2px; }
  .sig-address { font-size: 19px; line-height: 31px; margin-top: 10px; }
  .sig-contact { font-size: 19px; line-height: 31px; margin-top: 11px; }
  .sig-contact .contact-line { gap: 7px; }
  .sig-social { position: absolute; left: 999px; top: 112px; width: 89px; }
  .social-link { position: relative; height: 24px; margin-bottom: 10px; display: flex; align-items: center; }
  .social-link::before { content: ""; position: absolute; left: 10px; right: 0; top: 4px; height: 17px; background: var(--red); }
  .social-link i { position: relative; width: 24px; height: 24px; border-radius: 50%; border: 3px solid var(--red); background: #fff; display: block; flex: none; }
  .social-link span { position: relative; margin-left: 4px; font-size: 10px; font-weight: 600; color: #fff; }
  .sig-wave { position: absolute; left: 0; bottom: 0; }
</style>
</head>
<body>

<section class="letterhead">
  <div class="brand"><span class="brand-dot"></span>Trexolan Bearings Ltd</div>

  <div class="lh-contact">
    <div>Your Company Address</div>
    <div>Road No. 18, PO 2210, BD</div>
    <div class="contact-line" style="margin-top:2px"><svg width="8" height="8" viewBox="0 0 10 10"><path d="M1 3 Q5 0 9 3 L8 4.5 L6.5 3.8 L6.5 3 Q5 2.5 3.5 3 L3.5 3.8 L2 4.5 Z M2.5 5 H7.5 L8.5 9 H1.5 Z" fill="var(--red)"/></svg><span>(555) 010-2040</span></div>
    <div class="contact-line"><svg width="8" height="7" viewBox="0 0 10 8"><rect width="10" height="8" fill="var(--red)"/><path d="M0 0 L5 4.5 L10 0" stroke="#fff" fill="none"/></svg><span>hello@trexolan.co.uk</span></div>
    <div class="contact-line"><svg width="8" height="8" viewBox="0 0 10 10"><circle cx="5" cy="5" r="5" fill="var(--red)"/><path d="M1 5 H9 M5 0.5 V9.5" stroke="#fff" stroke-width=".8"/></svg><span>www.<span class="web-accent">trexolan</span>.co.uk</span></div>
  </div>
  <div class="lh-rule"></div>

  <article class="letter">
    <div class="letter-date">February, 12, 2021</div>
    <div class="letter-to">To</div>
    <div class="recipient-name">MR. ORIN VALDE</div>
    <div class="recipient-detail">Founder<br>82 Harlow Row, Ste #14,<br>Easton Vale, EV 20417<br>Post Code 7316</div>
    <div class="letter-body">
      <p>I'm Teo. I am a student. In this year I passed my Bed Honers. Now I'm try to divlope my life by this freelancer platfrom. I live in Bangladesh. I'm Teo. I am a student. In this year I passed my Bed rom. I live in Bangladesh. I'm Teo. I am a student.</p>
      <p>I'm Teo. I am a student. In this year I passed my Bed Honers. Now I'm try to divlope my life by this freelancer platfrom. I live in Bangladesh. I'm Teo. Now I'm try to divlope my life by this freelancer platfrom. I live in Bangladesh. I'm Teo. I am a student. In this year I passed my Bed Honers. Now I'm try to divlope my life by this freelancer platfrom. I live in Bangladesh. I am a student. In this year I passed my Bed Honers.</p>
      <p>I'm Teo. I am a student. In this year I passed my Bed Honers. Now I'm try to divlope my life by this freelancer platfrom. I live in Bangladesh. I'm Teo. Now I'm try to divlope my life by this freelancer platfrom. I live in Bangladesh. I'm Teo. I am a student. I am a student. In this year I passed my Bed Honers. Now I'm try to divlope my life by this freelancer platfrom. I live in</p>
      <p>I'm Teo. I am a student. In this year I passed my Bed Honers. Now I'm try to divlope my life by this freelancer platfrom. I live in Bangladesh. I'm Teo. Now I'm try to divlope my life by this freelancer platfrom.</p>
    </div>
    <div class="sign-off">Best Regurd</div>
    <div class="signature-area" role="img" aria-label="Handwritten signature of Lenna"></div>
  </article>

  <div class="lh-social">
    <span class="lh-social-item"><i></i>Vorlant</span>
    <span class="lh-social-item"><i></i>Pelmora</span>
    <span class="lh-social-item"><i></i>zandoro</span>
  </div>
  <div class="cert-badge" role="img" aria-label="qel certification badge"></div>
  <div class="cert-number">Certificat No: 481205637</div>

  <svg class="lh-wave" width="485" height="70" viewBox="0 0 485 70">
    <path d="M0 4 C150 24 330 40 485 14 C330 46 150 42 0 22 Z" fill="var(--dark)"/>
    <path d="M0 26 C150 46 330 48 485 18 L485 70 L0 70 Z" fill="var(--red)"/>
  </svg>
</section>

<section class="signature-card small">
  <div class="brand"><span class="brand-dot"></span>Trexolan Bearings Ltd</div>
  <div class="sig-divider"></div>
  <div class="sig-details">
    <div class="sig-name">DARA QUELL</div>
    <div class="sig-role">CEO/ Founder</div>
    <div class="sig-address">Your Company Address<br>Road No. 18, PO 2210, BD</div>
    <div class="sig-contact">
      <div class="contact-line"><svg width="18" height="16" viewBox="0 0 10 10"><path d="M1 3 Q5 0 9 3 L8 4.5 L6.5 3.8 L6.5 3 Q5 2.5 3.5 3 L3.5 3.8 L2 4.5 Z M2.5 5 H7.5 L8.5 9 H1.5 Z" fill="var(--red)"/></svg><span>(555) 010-2040</span></div>
      <div class="contact-line"><svg width="18" height="14" viewBox="0 0 10 8"><rect width="10" height="8" fill="var(--red)"/><path d="M0 0 L5 4.5 L10 0" stroke="#fff" fill="none"/></svg><span>hello@trexolan.co.uk</span></div>
      <div class="contact-line"><svg width="18" height="18" viewBox="0 0 10 10"><circle cx="5" cy="5" r="5" fill="var(--red)"/><path d="M1 5 H9 M5 0.5 V9.5" stroke="#fff" stroke-width=".8"/></svg><span>www.<span class="web-accent">trexolan</span>.co.uk</span></div>
    </div>
  </div>
  <div class="sig-social">
    <div class="social-link"><i></i><span>Vorlant</span></div>
    <div class="social-link"><i></i><span>Pelmora</span></div>
    <div class="social-link"><i></i><span>zandoro</span></div>
  </div>
  <svg class="sig-wave" width="1088" height="120" viewBox="0 0 1088 120">
    <path d="M0 37 C300 62 700 72 1088 46 C700 80 300 80 0 65 Z" fill="var(--dark)"/>
    <path d="M0 68 C300 88 700 88 1088 52 L1088 120 L0 120 Z" fill="var(--red)"/>
  </svg>
</section>

<section class="signature-card large">
  <div class="brand"><span class="brand-dot"></span>Trexolan Bearings Ltd</div>
  <div class="sig-divider"></div>
  <div class="sig-details">
    <div class="sig-name">DARA QUELL</div>
    <div class="sig-role">CEO/ Founder</div>
    <div class="sig-address">Your Company Address<br>Road No. 18, PO 2210, BD</div>
    <div class="sig-contact">
      <div class="contact-line"><svg width="18" height="16" viewBox="0 0 10 10"><path d="M1 3 Q5 0 9 3 L8 4.5 L6.5 3.8 L6.5 3 Q5 2.5 3.5 3 L3.5 3.8 L2 4.5 Z M2.5 5 H7.5 L8.5 9 H1.5 Z" fill="var(--red)"/></svg><span>(555) 010-2040</span></div>
      <div class="contact-line"><svg width="18" height="14" viewBox="0 0 10 8"><rect width="10" height="8" fill="var(--red)"/><path d="M0 0 L5 4.5 L10 0" stroke="#fff" fill="none"/></svg><span>hello@trexolan.co.uk</span></div>
      <div class="contact-line"><svg width="18" height="18" viewBox="0 0 10 10"><circle cx="5" cy="5" r="5" fill="var(--red)"/><path d="M1 5 H9 M5 0.5 V9.5" stroke="#fff" stroke-width=".8"/></svg><span>www.<span class="web-accent">trexolan</span>.co.uk</span></div>
    </div>
  </div>
  <div class="sig-social">
    <div class="social-link"><i></i><span>Vorlant</span></div>
    <div class="social-link"><i></i><span>Pelmora</span></div>
    <div class="social-link"><i></i><span>zandoro</span></div>
  </div>
  <svg class="sig-wave" width="1088" height="120" viewBox="0 0 1088 120">
    <path d="M0 37 C300 62 700 72 1088 46 C700 80 300 80 0 65 Z" fill="var(--dark)"/>
    <path d="M0 68 C300 88 700 88 1088 52 L1088 120 L0 120 Z" fill="var(--red)"/>
  </svg>
</section>

</body>
</html>
```